Einladungskarten-Design für Reinigung & Gebäudemangement
Zielgruppe:
Potentielle Kunden/Entscheider Einrichtungsleiter, Geschäftführer für den Bereich Alten- und Pflegeheime, Krankenhäuser.
Das Angebot geht über Verpflegungslösung, Reinigung, Gebäudemangement und Innovationen (z.B. zum Thema Digitalisierung, Roboting, .....).
Der Claim des Unternehmens ist 'Quality of Life Services = Services der Lebensqualität'
Aufgabenstellung
Gerne Pop-Up oder auch Relief - hochwertige Haptik von Umschlag und Karte ggf. Sonderformat d.h. nicht Standard DL quer
Sollte aber dennoch klassich gut wirken.
Die persönliche Note erhält die Karte durch handschriftliche Personalisierung durch den Sales Mitarbeiter.
Die Karte soll folgenden Text enthalten.
Text:
Das neue Jahr liegt vor Ihnen.
Nutzen Sie seine Chancen und ergreifen Sie seine Möglichkeiten.
Beispielsweise mit einem Gespräch
über inspierierende Ideen und neue Konzepte zur Steigerung der Lebensqualität
in Ihrem Hause.
Wir freuen uns mit Ihnen in Kontakt zu sein.
Der Umschlag soll Absenderadresse und Logo enthalten - dies wird nach Prämierung bekannt gegeben.
Natürlich kann auf der Rückseite der Karte auch das Logo mit Claim aufgedruckt werden.
Alle Bildrechte sollen nach Prämierung auf den Auftraggeber übergehen.

```html
<!DOCTYPE html>
<html lang="de">
<head>
<meta charset="utf-8">
<title>Einladungskarte – Lebensqualität</title>
<link rel="stylesheet" href="https://fonts.googleapis.com/css2?family=EB+Garamond:wght@400&display=swap">
<style>
  :root {
    --paper: #ffffff;
    --ink: #1a1a1a;
    --gold-deep: #b8931f;
    --gold-mid: #d4b13a;
    --gold-light: #f3e07c;
    --gold-shade: #a3811a;
  }
  html, body {
    margin: 0;
    padding: 0;
    width: 1200px;
    height: 1200px;
    overflow: hidden;
    background: var(--paper);
  }
  .card {
    position: relative;
    width: 1200px;
    height: 1200px;
    background: var(--paper);
    font-family: "EB Garamond", Garamond, serif;
    color: var(--ink);
  }
  .gold-band {
    position: absolute;
    left: 0;
    width: 1200px;
    background:
      repeating-linear-gradient(180deg, rgba(255,255,255,0.08) 0 2px, rgba(0,0,0,0.05) 2px 4px),
      linear-gradient(90deg, var(--gold-shade) 0%, var(--gold-mid) 14%, var(--gold-deep) 30%, var(--gold-mid) 48%, var(--gold-light) 72%, var(--gold-mid) 84%, var(--gold-deep) 100%);
  }
  .gold-band--top { top: 0; height: 280px; }
  .gold-band--bottom { top: 1096px; height: 104px; }
  .message {
    position: absolute;
    top: 288px;
    left: 0;
    width: 1200px;
    margin: 0;
    text-align: center;
    font-size: 46px;
    line-height: 61px;
    font-weight: 400;
  }
  .message p { margin: 0; }
  .message .closing { margin-top: 61px; }
</style>
</head>
<body>
  <main class="card">
    <div class="gold-band gold-band--top"></div>
    <section class="message">
      <p>Nutzen Sie seine Chancen<br>
      und ergreifen Sie seine Möglichkeiten.<br>
      Beispielsweise mit einem Gespräch<br>
      über inspierierende Ideen<br>
      und neue Konzepte zur Steigerung<br>
      der Lebensqualität<br>
      in Ihrem Hause.</p>
      <p class="closing">Wir freuen uns mit Ihnen in Kontakt zu sein.</p>
    </section>
    <div class="gold-band gold-band--bottom"></div>
  </main>
</body>
</html>
```